Barrister Letterhead incorporating existing logo/design

Require new letterhead template to incorporate logo and information on 'Letter 2015' word document. Currently the information on the letterhead is very busy and would like a cleaner look.
Must look good in black and white, and colour when printed.

Target Market(s)

Professional

Industry/Entity Type

Legal

Requirements
Must have
• Clean professional look.

```html
<!DOCTYPE html>
<html lang="en">
<head>
<meta charset="utf-8">
<title>Hartley Chambers Letterhead</title>
<link href="https://fonts.googleapis.com/css2?family=Cinzel:wght@400;700&display=swap" rel="stylesheet">
<style>
  :root {
    --navy: #1b2440;
    --ink: #2a3048;
    --paper: #ffffff;
    --backdrop: #e9e8e5;
    --mark-grey: #c4c7cd;
    --mark-frame: #d9dbdf;
  }
  * { margin: 0; padding: 0; box-sizing: border-box; }
  html, body {
    width: 1200px; height: 1200px; overflow: hidden;
    background: var(--backdrop);
    font-family: "Cinzel", serif;
    color: var(--ink);
  }
  .sheet {
    position: absolute; left: 176px; top: 0;
    width: 848px; height: 1200px;
    background: var(--paper);
  }
  .brand { position: absolute; left: 52px; top: 68px; display: flex; align-items: center; gap: 6px; }
  .brand-square { width: 50px; height: 50px; background: var(--navy); }
  .brand-name {
    color: var(--navy); font-weight: 400; font-size: 30px; line-height: 26px;
    text-transform: uppercase; letter-spacing: 0.5px;
  }
  .barrister { position: absolute; left: 300px; top: 56px; color: var(--navy); font-size: 16px; line-height: 24px; }
  .barrister-name { font-weight: 700; font-size: 16px; text-transform: uppercase; }
  .barrister-line { text-transform: uppercase; }
  .contact { position: absolute; left: 508px; top: 50px; font-size: 12px; line-height: 16px; color: var(--navy); text-transform: uppercase; }
  .contact-address { margin-bottom: 12px; }
  .contact-label { font-weight: 700; }
  .letter { position: absolute; left: 72px; font-size: 18px; color: var(--ink); }
  .date { top: 266px; }
  .recipient { top: 346px; line-height: 26px; }
  .via { top: 503px; }
  .salutation { top: 580px; }
  .subject { top: 628px; }
  .subject span { margin-left: 12px; text-transform: uppercase; }
  .closing { top: 704px; }
  .signatory { top: 858px; line-height: 28px; }
  .signatory-name { font-weight: 700; color: var(--navy); text-transform: uppercase; font-size: 19px; }
  .disclaimer { position: absolute; left: 74px; top: 984px; font-size: 12px; letter-spacing: 0.3px; color: var(--navy); }
  .corner-mark {
    position: absolute; left: 676px; top: 1016px;
    width: 160px; height: 140px;
    background: var(--mark-grey);
    outline: 3px solid var(--mark-frame); outline-offset: 2px;
  }
</style>
</head>
<body>
  <main class="sheet">
    <header>
      <div class="brand">
        <span class="brand-square"></span>
        <span class="brand-name">Hartley<br>Chambers</span>
      </div>
      <div class="barrister">
        <div class="barrister-name">Elliot Marsh LL.B.</div>
        <div class="barrister-line">Barrister-at-Law</div>
        <div class="barrister-line">ABN 12 345 678 901</div>
      </div>
      <div class="contact">
        <div class="contact-address">Level 2 14 Hartley Street, Kingsford<br>P.O. Box 218, Kingsford. Q 4870</div>
        <div><span class="contact-label">Telephone:</span> 07 4500 0123</div>
        <div><span class="contact-label">Fax:</span> 07 4500 0456</div>
        <div><span class="contact-label">Email:</span> emarsh@kingsfordbar.com.au</div>
        <div><span class="contact-label">Website:</span> www.hartleychambers.com.au</div>
      </div>
    </header>

    <p class="letter date">6 November 2015</p>
    <p class="letter recipient">Attention:<br>Address<br>Address<br>Address</p>
    <p class="letter via">Via email:</p>
    <p class="letter salutation">Dear &nbsp;&nbsp;&nbsp;&nbsp;&nbsp;&nbsp;&nbsp;&nbsp;&nbsp;&nbsp;&nbsp;,</p>
    <p class="letter subject">Re:<span>Matter</span></p>
    <p class="letter closing">Yours faithfully,</p>
    <p class="letter signatory"><span class="signatory-name">Elliot Marsh</span><br>Chambers</p>

    <footer>
      <p class="disclaimer">Liability limited by a scheme approved under professional standards legislation</p>
      <div class="corner-mark" aria-hidden="true"></div>
    </footer>
  </main>
</body>
</html>
```